Corvane Stationery Design

We need design for our stationary, including:
1) Letterhead
- A4/Letter size in landscape and portrait letterhead
- The letterhead must be in a word file, and the address should be editable using the Felixti or Perpetua Titling TTF
- The output file should be in .docx and in .ai.
2) Business card
- The business card will be printed in white paper and single face only, so there should be nothing on the reverse side.
3) Envelope (sizes A4, Letter, and small document)
Please refer to the picture showing some samples of stationary with designs that would fulfill our wish.
We're including the logo in .AI.
Thanks
Target Market(s)
High end investors
Industry/Entity Type
Landscape
Look and feel

```html
<!DOCTYPE html>
<html lang="en">
<head>
<meta charset="utf-8">
<title>Corvane Capital Partners — Stationery</title>
<link rel="stylesheet" href="https://fonts.googleapis.com/css2?family=Cormorant+Garamond:wght@500&display=swap">
<style>
  :root {
    --backdrop: #e4e4e4;
    --paper: #ffffff;
    --paper-edge: #cfcfcf;
    --ink: #5a5a5a;
    --accent: #1b8db1;
    --rule-grey: #8a8a8a;
    --window: #eceeed;
    --window-edge: #9a9a9a;
  }
  * { box-sizing: border-box; margin: 0; padding: 0; }
  html, body { width: 1200px; height: 900px; overflow: hidden; }
  body {
    background: var(--backdrop);
    font-family: "Cormorant Garamond", Garamond, serif;
    font-weight: 500;
    color: var(--ink);
    position: relative;
  }
  .sheet {
    position: absolute;
    background: var(--paper);
    border: 1px solid var(--paper-edge);
  }

  /* Company name: one line, one colour, one weight, with a plain square */
  .company-name {
    display: flex; align-items: center; gap: 8px;
    color: var(--ink); line-height: 1; white-space: nowrap;
    letter-spacing: 0.01em;
  }
  .company-name .marker { display: block; background: var(--ink); flex: none; }

  /* Letterhead */
  .letterhead { left: 80px; top: 44px; width: 566px; height: 798px; }
  .letterhead .company-name {
    position: absolute; left: 0; right: 0; top: 52px;
    justify-content: center; font-size: 22px;
  }
  .letterhead .company-name .marker { width: 8px; height: 8px; }
  .letterhead .head-rule {
    position: absolute; left: 27px; right: 27px; top: 86px;
    border-top: 1px solid var(--accent);
  }
  .letterhead .foot-rule {
    position: absolute; left: 27px; right: 27px; top: 714px;
    border-top: 1px solid var(--rule-grey);
  }
  .letterhead .footer {
    position: absolute; left: 0; right: 0; top: 727px;
    text-align: center; font-size: 7.5px; line-height: 10px; letter-spacing: 0.04em;
    font-style: normal;
  }
  .letterhead .footer .gap { margin-top: 5px; }
  .accent { color: var(--accent); }

  /* Business card */
  .card { left: 726px; top: 331px; width: 242px; height: 136px; }
  .card .company-name { position: absolute; left: 20px; top: 20px; font-size: 12px; gap: 5px; }
  .card .company-name .marker { width: 5px; height: 5px; }

  /* Contact block shared by card and envelope */
  .contact {
    position: absolute; text-align: right; color: var(--ink);
    letter-spacing: 0.03em; font-style: normal;
  }
  .contact .row { display: flex; justify-content: flex-end; align-items: center; gap: 3px; white-space: nowrap; }
  .contact svg { fill: var(--accent); flex: none; }
  .contact .group + .group { margin-top: 5px; }
  .card .contact { right: 10px; top: 76px; font-size: 5.5px; line-height: 6.8px; }
  .card .contact svg { width: 5px; height: 5px; }

  /* Envelope */
  .envelope { left: 548px; top: 550px; width: 566px; height: 266px; }
  .envelope .company-name { position: absolute; left: 40px; top: 44px; font-size: 22px; }
  .envelope .company-name .marker { width: 8px; height: 8px; }
  .envelope .window {
    position: absolute; left: 40px; top: 126px; width: 228px; height: 116px;
    background: var(--window); border: 1px solid var(--window-edge); border-radius: 14px;
  }
  .envelope .contact { right: 42px; top: 188px; font-size: 7px; line-height: 8.4px; }
  .envelope .contact svg { width: 6px; height: 6px; }
</style>
</head>
<body>

<svg width="0" height="0" style="position:absolute" aria-hidden="true">
  <defs>
    <symbol id="icon-pin" viewBox="0 0 10 10"><path d="M5 0a3.5 3.5 0 0 0-3.5 3.5C1.5 6 5 10 5 10s3.5-4 3.5-6.5A3.5 3.5 0 0 0 5 0zm0 5a1.5 1.5 0 1 1 0-3 1.5 1.5 0 0 1 0 3z"/></symbol>
    <symbol id="icon-phone" viewBox="0 0 10 10"><path d="M3 0h4v10H3zM3.8 1v7h2.4V1z"/></symbol>
    <symbol id="icon-fax" viewBox="0 0 10 10"><path d="M3 0h4v3H3zM1 3.5h8V9H1zM3 6h4v4H3z"/></symbol>
    <symbol id="icon-mail" viewBox="0 0 10 10"><path d="M0 2h10v6H0zM1 3l4 2.6L9 3v-.2H1z"/></symbol>
    <symbol id="icon-web" viewBox="0 0 10 10"><circle cx="5" cy="5" r="5"/></symbol>
  </defs>
</svg>

<section class="sheet letterhead" aria-label="Letterhead">
  <div class="company-name"><span class="marker"></span>Corvane Capital Partners</div>
  <div class="head-rule"></div>
  <div class="foot-rule"></div>
  <address class="footer">
    <div>48 HARBOR LANE, BROOKFIELD, NEW YORK 10452</div>
    <div><span class="accent">P</span> 212 640 31 70 &nbsp;<span class="accent">F</span> 212 640 31 71</div>
    <div class="gap">INFO@CORVANE-CAPITAL.COM &nbsp;<span class="accent">WWW.CORVANE-CAPITAL.COM</span></div>
  </address>
</section>

<section class="sheet card" aria-label="Business card">
  <div class="company-name"><span class="marker"></span>Corvane Capital Partners</div>
  <address class="contact">
    <div class="group">
      <div class="row">48 HARBOR LANE <svg><use href="#icon-pin"/></svg></div>
      <div class="row">BROOKFIELD, NEW YORK 10452 <svg style="visibility:hidden"><use href="#icon-pin"/></svg></div>
      <div class="row">212 640 31 70 <svg><use href="#icon-phone"/></svg></div>
      <div class="row">212 640 31 71 <svg><use href="#icon-fax"/></svg></div>
    </div>
    <div class="group">
      <div class="row">INFO@CORVANE-CAPITAL.COM <svg><use href="#icon-mail"/></svg></div>
      <div class="row">WWW.CORVANE-CAPITAL.COM <svg><use href="#icon-web"/></svg></div>
    </div>
  </address>
</section>

<section class="sheet envelope" aria-label="Envelope">
  <div class="company-name"><span class="marker"></span>Corvane Capital Partners</div>
  <div class="window"></div>
  <address class="contact">
    <div class="group">
      <div class="row">48 HARBOR LANE <svg><use href="#icon-pin"/></svg></div>
      <div class="row">BROOKFIELD, NEW YORK 10452 <svg style="visibility:hidden"><use href="#icon-pin"/></svg></div>
      <div class="row">212 640 31 70 <svg><use href="#icon-phone"/></svg></div>
      <div class="row">212 640 31 71 <svg><use href="#icon-fax"/></svg></div>
    </div>
    <div class="group">
      <div class="row">INFO@CORVANE-CAPITAL.COM <svg><use href="#icon-mail"/></svg></div>
      <div class="row">WWW.CORVANE-CAPITAL.COM <svg><use href="#icon-web"/></svg></div>
    </div>
  </address>
</section>

</body>
</html>
```